Business Card (double-sided) and Stationary Design for dental office

1) Business Card Design: We need a business card design for a dental specialty office.
Texts should contain:
The name of our office "Bayhaven Grins Orthodontics"
Tagline: "Specialist in Orthodontic and Maxillofacial Orthopedics"
Tag line: "Creating "Talvering" smiles for Children and Adults"
Doctor name: "Doctor Name"
Office Address:
"123 Street Name
City, State Zip code"
Office email address: office@bayhavengrins.com
Website: www.bayhavengrins.com

We will provide the full office address once the design is selected
Theme: beach, paradise, coastal, wave
We would like to have some creativity in design. Some acceptable ideas: front page: logo and office name. Back page: more detail information, and map to office in form of an island. Please see sample from our other location, but you DON'T HAVE TO USE OR COPY THE SAME CONCEPT.

IF POSSIBLE, PLEASE SUBMIT AT LEAST TWO CONCEPTS: ONE WITH THE BACK LOOKING SIMILAR TO WHAT IS IN THE SAMPLE, AND ONE DIFFERENT.

Color: designer to choose. We have different shade of blues and sand color in our office. Please see logo.

2) Please also design a matching set of stationary that compliment the business card and our logo.

Target Market(s)

Dental

Contact Information for Business Card

See descriptions

Font styles to use
Other font styles liked:
• Matching texts in logo

Colors
0054AA
0677BA
7BADD7
CADEEF
E8F1F8
0094D4
00A9DD
6FCCEA
C7EBF8
E9F6FB
00AB8E
00BBA5
67D7C9
C6EFE9
E9F9F6

Requirements
Must have
• Double-sided
Nice to have
• Beach coastal theme
Should not have
• Any shape or drawing of of tooth or teeth. We don’t need these. You don't necessarily have to just cut and paste the logo art and text as a whole, you have the liberty to rearrange the text.

```html
<!DOCTYPE html>
<html lang="en">
<head>
<meta charset="utf-8">
<title>Bayhaven Grins Orthodontics – Business Card</title>
<link href="https://fonts.googleapis.com/css2?family=Raleway:ital,wght@0,400;0,600;0,700;1,700&family=Nunito:wght@700;800&display=swap" rel="stylesheet">
<style>
  :root {
    --page-bg: #e6e6e6;
    --card-dark: #1b1b1c;
    --brand-blue: #3a8fad;
    --brand-blue-text: #4a9cc0;
    --mint: #5ad6c6;
    --mint-light: #7be0d3;
    --sand: #efe7cf;
    --white: #ffffff;
    --ink-grey: #8a8a8a;
    --line-grey: #9a9a9a;
    --text-light: #f1f1f1;
  }
  * { margin: 0; padding: 0; box-sizing: border-box; }
  html, body { width: 1200px; height: 842px; overflow: hidden; background: var(--page-bg); }
  .canvas {
    width: 1200px; height: 842px;
    display: flex; align-items: center; justify-content: center; gap: 30px;
  }
  .card {
    position: relative; width: 560px; height: 320px; overflow: hidden;
    box-shadow: 0 6px 18px rgba(0,0,0,.22);
  }

  /* Front */
  .card-front { background: var(--card-dark); font-family: 'Raleway', sans-serif; }
  .brand { position: absolute; left: 40px; top: 72px; width: 220px; text-align: center; }
  .brand-dot { width: 70px; height: 70px; border-radius: 50%; background: var(--brand-blue); margin: 0 auto 14px; }
  .brand-name {
    font-family: 'Nunito', sans-serif; font-weight: 800; color: var(--brand-blue-text);
    font-size: 27px; line-height: 1.05; letter-spacing: .5px;
  }
  .divider { position: absolute; left: 275px; top: 38px; width: 1px; height: 180px; background: #3a3a3a; }
  .contact { position: absolute; left: 298px; top: 56px; color: var(--text-light); }
  .contact-name { font-weight: 700; font-size: 23px; color: var(--brand-blue-text); line-height: 1; }
  .contact-role { font-size: 14px; margin-top: 4px; }
  .contact-address { font-size: 14px; line-height: 1.3; margin-top: 14px; }
  .contact-links { margin-top: 14px; font-size: 14px; line-height: 1.55; }
  .contact-links li { list-style: none; display: flex; align-items: center; gap: 7px; }
  .contact-links svg { width: 14px; height: 14px; flex: none; }
  .tagline-band {
    position: absolute; left: 0; right: 0; top: 240px; height: 34px; background: var(--brand-blue);
    display: flex; align-items: center; justify-content: center;
    color: var(--white); font-style: italic; font-weight: 700; font-size: 17px;
  }

  /* Back */
  .card-back { background: var(--white); font-family: 'Raleway', sans-serif; }
  .card-back .shore { position: absolute; inset: 0; }
  .appointment { position: absolute; left: 40px; top: 50px; }
  .appointment-title { color: var(--brand-blue); font-size: 20px; font-weight: 600; letter-spacing: .3px; }
  .appointment-field { display: flex; align-items: flex-end; gap: 8px; color: var(--ink-grey); font-size: 14px; margin-top: 14px; }
  .appointment-field .fill-line { width: 230px; border-bottom: 1.5px dotted var(--line-grey); height: 10px; }
  .back-tagline {
    position: absolute; left: 40px; top: 232px; color: var(--white);
    font-family: 'Nunito', sans-serif; font-weight: 800; font-size: 19px; line-height: 1.2;
  }
  .location-map { position: absolute; left: 340px; top: 120px; width: 200px; height: 180px; background: var(--mint-light); border-radius: 10px; opacity: .55; }
</style>
</head>
<body>
<main class="canvas">

  <section class="card card-front" aria-label="Business card front">
    <div class="brand">
      <div class="brand-dot"></div>
      <div class="brand-name">Bayhaven Grins<br>Orthodontics</div>
    </div>
    <div class="divider"></div>
    <div class="contact">
      <div class="contact-name">Marcus Ellery</div>
      <div class="contact-role">Managing Director</div>
      <div class="contact-address">123 Street Name<br>City, State Zip code</div>
      <ul class="contact-links">
        <li>
          <svg viewBox="0 0 16 16" aria-hidden="true"><rect x="1" y="3" width="14" height="10" fill="none" stroke="#4a9cc0" stroke-width="1.6"/><path d="M1 3l7 6 7-6" fill="none" stroke="#4a9cc0" stroke-width="1.6"/></svg>
          office@bayhavengrins.com
        </li>
        <li>
          <svg viewBox="0 0 16 16" aria-hidden="true"><circle cx="8" cy="8" r="6.5" fill="none" stroke="#4a9cc0" stroke-width="1.4"/><ellipse cx="8" cy="8" rx="3" ry="6.5" fill="none" stroke="#4a9cc0" stroke-width="1.2"/><path d="M1.5 8h13M2.5 4.8h11M2.5 11.2h11" stroke="#4a9cc0" stroke-width="1.1"/></svg>
          www.bayhavengrins.com
        </li>
      </ul>
    </div>
    <div class="tagline-band">Specialist in Orthodontic and Maxillofacial Orthopedics</div>
  </section>

  <section class="card card-back" aria-label="Business card back">
    <svg class="shore" viewBox="0 0 560 320" preserveAspectRatio="none" aria-hidden="true">
      <path d="M0 210 C60 205 90 185 130 170 C180 150 230 120 270 105 C330 80 380 80 430 60 C480 40 520 30 560 35 V320 H0 Z" fill="var(--sand)"/>
      <path d="M0 224 C60 220 95 200 135 185 C185 165 235 135 275 120 C335 96 385 96 435 76 C485 56 525 46 560 50 V320 H0 Z" fill="var(--mint)"/>
    </svg>
    <div class="appointment">
      <div class="appointment-title">NEXT APPOINTMENT</div>
      <div class="appointment-field"><span>Name</span><span class="fill-line"></span></div>
      <div class="appointment-field"><span>Date</span><span class="fill-line"></span></div>
    </div>
    <div class="location-map" role="img" aria-label="Street map showing the office location with a pin"></div>
    <div class="back-tagline">Creating Talvering<br>Smiles for Children<br>and Adults</div>
  </section>

</main>
</body>
</html>
```